Need a Zine cover designed

I’m looking for someone who can design an eye catching and original zine cover. Incorporating the logo I included below. I’m not 100% sure which logo I want to use on the cover, if it’s possible to see how you incorporate the logos on a sample will make it easier for me to decide. Thank you for your time.
For the second logo I’m unsure how to remove the grey background, but I do not want it included in the zine cover
The title of the zine is:
Amber Crossroads
perspectives of culture, life, & love

```html
<!DOCTYPE html>
<html lang="en">
<head>
<meta charset="utf-8">
<title>Amber Crossroads — Zine Cover</title>
<link rel="stylesheet" href="https://fonts.googleapis.com/css2?family=Archivo+Black&family=Bebas+Neue&display=swap">
<style>
  :root {
    --backdrop: #1b1b1b;
    --paper: #ffffff;
    --ink: #1a1a1a;
    --mint: #5fbf8f;
    --amber: #f08a24;
  }
  html, body {
    margin: 0;
    padding: 0;
    width: 1200px;
    height: 1200px;
    overflow: hidden;
    background: var(--backdrop);
  }
  .cover {
    position: absolute;
    left: 289px;
    top: 120px;
    width: 621px;
    height: 960px;
    background: var(--paper);
    box-sizing: border-box;
    border: 1px solid #000;
  }
  .club-mark {
    position: absolute;
    left: 0;
    right: 0;
    top: 118px;
    display: flex;
    align-items: center;
    justify-content: center;
    gap: 10px;
    font-family: "Archivo Black", sans-serif;
    font-size: 26px;
    color: var(--ink);
    letter-spacing: 0.5px;
  }
  .club-mark .dot {
    width: 16px;
    height: 16px;
    border-radius: 50%;
    background: var(--ink);
  }
  .title {
    position: absolute;
    left: 0;
    top: 0;
    width: 621px;
    height: 960px;
  }
  .title text {
    font-family: "Archivo Black", sans-serif;
    font-size: 74px;
    letter-spacing: -2px;
  }
  .title .echo {
    fill: none;
    stroke: var(--amber);
    stroke-width: 1.2;
  }
  .title .face { fill: var(--mint); }
  .tagline {
    position: absolute;
    left: 0;
    right: 0;
    top: 842px;
    text-align: center;
    font-family: "Bebas Neue", sans-serif;
    font-size: 46px;
    line-height: 1;
    letter-spacing: 6px;
    color: var(--ink);
    margin: 0;
  }
</style>
</head>
<body>
  <main class="cover">
    <div class="club-mark">
      <span class="dot"></span>
      <span class="club-name">Leisure Society</span>
    </div>

    <svg class="title" viewBox="0 0 621 960" aria-label="Amber Crossroads">
      <g transform="rotate(-9 311 500)">
        <text class="echo" x="318" y="478" text-anchor="middle">AMBER</text>
        <text class="face" x="330" y="490" text-anchor="middle">AMBER</text>
        <text class="echo" x="302" y="558" text-anchor="middle">CROSSROADS</text>
        <text class="face" x="314" y="570" text-anchor="middle">CROSSROADS</text>
      </g>
    </svg>

    <p class="tagline">Perspectives of culture, life, &amp; love</p>
  </main>
</body>
</html>
```